Software company specialized in data analytics and professional services

We need a landing page design for our business. It should include our logo design. It should have multiple sections :
- stylish head
- what we do (data analytics software, professional services)
- contact form

Target Market(s)

Companies, B2B

Industry/Entity Type

Data

Number of Pages Required

1 page

Font styles to use
Sans Serif

Requirements
Must have
• Dark theme
Should not have
• Gradients on buttons

```html
<!DOCTYPE html>
<html lang="en">
<head>
<meta charset="utf-8">
<title>Northgrid — Data Analytics</title>
<link rel="stylesheet" href="https://fonts.googleapis.com/css2?family=Archivo:wght@500;600;700;800&family=Inter:wght@400;500;600&display=swap">
<style>
:root{
  --ink:#2f2f3a;
  --navy:#0f0a45;
  --navy-card:#1a1263;
  --purple:#7a1fd6;
  --magenta:#d10ea8;
  --teal:#0e6f96;
  --pink-soft:#fbe0f3;
  --line:#ececf2;
  --white:#ffffff;
  --muted:#5a5a66;
}
*{margin:0;padding:0;box-sizing:border-box}
html,body{width:679px;height:1200px;overflow:hidden;background:var(--white)}
body{position:relative;font-family:"Inter",sans-serif;color:var(--ink)}
.abs{position:absolute}
.logo{font-family:"Archivo",sans-serif;font-weight:800;color:var(--magenta);letter-spacing:.5px}
.header-logo{left:71px;top:11px;font-size:19px}
.header-btn{left:507px;top:10px;width:101px;height:23px;border:1px solid var(--purple);border-radius:12px;font-size:6px;font-weight:600;letter-spacing:1.5px;color:var(--purple);display:flex;align-items:center;justify-content:center}
.header-rule{left:71px;top:42px;width:537px;height:1px;background:var(--line)}
.hero-title{left:71px;top:86px;width:320px;font-family:"Archivo",sans-serif;font-weight:700;font-size:21.5px;line-height:23px;color:var(--ink)}
.hero-title em{font-style:normal;color:var(--purple)}
.hero-text{left:71px;top:168px;width:225px;font-size:6.3px;line-height:10.3px;color:var(--ink)}
.cta{left:71px;top:218px;width:101px;height:24px;border-radius:12px;background:var(--purple);color:var(--white);font-size:6px;font-weight:600;letter-spacing:1.5px;display:flex;align-items:center;justify-content:center}
.avatars{left:71px;top:280px;width:65px;height:27px}
.avatar{position:absolute;top:0;width:27px;height:27px;border-radius:50%;border:1.5px solid var(--white)}
.avatar-count{position:absolute;top:0;left:38px;width:27px;height:27px;border-radius:50%;background:var(--magenta);color:var(--white);font-size:7px;font-weight:600;display:flex;align-items:center;justify-content:center;border:1.5px solid var(--white)}
.reviews{left:143px;top:283px;font-size:6.8px;font-weight:600}
.reviews .stars{display:flex;gap:3px;margin-top:4px;align-items:center;font-weight:400;font-size:6px}
.dashboard{left:320px;top:50px;width:359px;height:342px;background:linear-gradient(160deg,#eef0fb 0%,#f7f8fd 55%,#fde9f6 100%);clip-path:polygon(4% 45%,100% 0,100% 100%,24% 100%)}
.stat-card{background:var(--white);border-radius:6px;box-shadow:0 6px 20px rgba(40,30,110,.12);padding:10px 12px}
.stat-card h4{font-family:"Archivo",sans-serif;font-size:8px;font-weight:600;color:var(--ink)}
.stat-card p{font-size:7.5px;font-weight:600;margin-top:2px}
.net{left:446px;top:70px;width:110px;height:74px;padding:8px 10px}
.net h4{font-size:7px}
.net p{color:var(--purple);font-size:6.5px}
.gross{left:278px;top:280px;width:132px;height:88px}
.gross p{color:var(--teal)}
.dark{left:0;top:392px;width:679px;height:389px;background:var(--navy)}
.dark-title{left:0;top:447px;width:679px;text-align:center;font-family:"Archivo",sans-serif;font-weight:700;font-size:20px;line-height:25px;color:var(--white)}
.dark-title em{font-style:normal;color:var(--magenta)}
.dark-text{left:180px;top:508px;width:319px;text-align:center;font-size:6.3px;line-height:10.3px;color:var(--white)}
.service{top:557px;width:263px;height:156px;background:var(--navy-card);border-radius:3px;box-shadow:0 8px 20px rgba(0,0,0,.25);text-align:center;color:var(--white)}
.service svg{margin-top:27px}
.service h3{font-family:"Archivo",sans-serif;font-weight:600;font-size:10.5px;margin-top:12px}
.service p{font-size:6.3px;line-height:10.3px;width:190px;margin:9px auto 0}
.toggle{top:702px;width:22px;height:22px;border-radius:50%;background:var(--teal);display:flex;align-items:center;justify-content:center}
.contact-title{left:71px;top:834px;font-family:"Archivo",sans-serif;font-weight:700;font-size:21px;line-height:23px;color:var(--ink)}
.contact-title em{font-style:normal;color:var(--purple)}
.contact-text{left:71px;top:892px;width:235px;font-size:6.3px;line-height:10.3px}
.info{left:71px;display:flex;gap:8px;align-items:flex-start}
.info .ico{width:23px;height:23px;border-radius:50%;background:var(--navy);display:flex;align-items:center;justify-content:center;flex:none}
.info h5{font-size:7px;font-weight:600;margin-top:2px}
.info span{display:block;font-size:6.3px;line-height:10px;margin-top:1px}
.form{left:346px;top:835px;width:262px;height:217px;background:var(--pink-soft)}
.form h3{position:absolute;top:17px;width:100%;text-align:center;font-family:"Archivo",sans-serif;font-weight:600;font-size:10.5px;color:var(--ink)}
.form .rule{position:absolute;left:100px;top:39px;width:63px;height:1px;background:var(--purple)}
.field{position:absolute;left:25px;width:212px;background:var(--white);font-size:6.5px;text-align:center;color:var(--ink)}
.send{position:absolute;left:120px;top:176px;width:22px;height:22px;border-radius:50%;background:var(--purple);display:flex;align-items:center;justify-content:center}
.footer{left:0;top:1108px;width:679px;height:92px;background:var(--navy)}
.footer-logo{left:71px;top:1136px;font-size:33px;color:var(--white)}
.copyright{right:71px;top:1149px;font-size:7px;color:var(--white)}
</style>
</head>
<body>
<header>
  <div class="abs logo header-logo">NORTHGRID</div>
  <div class="abs header-btn">CONTACT US</div>
  <div class="abs header-rule"></div>
</header>

<section class="hero">
  <div class="abs dashboard" role="img" aria-label="Tilted analytics dashboard interface with menu, session stats and device chart"></div>
  <h1 class="abs hero-title">CRAFTING <em>SUCCESS</em> STORIES THROUGH ADVANCED ANALYTICS</h1>
  <p class="abs hero-text">Lorem Ipsum is simply dummy text of the printing and typesetting industry. Lorem Ipsum has been the industry's standard dummy text ever since the 1500s,</p>
  <div class="abs cta">CONTACT US</div>
  <div class="abs avatars">
    <div class="avatar" style="left:0;background:#e7c3a8" role="img" aria-label="Customer photo"></div>
    <div class="avatar" style="left:13px;background:#d9a7c0" role="img" aria-label="Customer photo"></div>
    <div class="avatar" style="left:26px;background:#a9b8b0" role="img" aria-label="Customer photo"></div>
    <div class="avatar-count">1K+</div>
  </div>
  <div class="abs reviews">Happy Customers
    <div class="stars">
      <svg width="62" height="8" viewBox="0 0 62 8" fill="#f5b400">
        <g id="s"><polygon points="4,0 5,3 8,3 5.5,5 6.5,8 4,6 1.5,8 2.5,5 0,3 3,3"/></g>
        <use href="#s" x="10.5"/><use href="#s" x="21"/><use href="#s" x="31.5"/><use href="#s" x="42"/>
      </svg>
      <span>465+ Reviews</span>
    </div>
  </div>

  <div class="abs stat-card net">
    <h4>NET SALES</h4>
    <p>$2300</p>
    <svg width="90" height="36" viewBox="0 0 90 36">
      <defs><linearGradient id="gp" x1="0" y1="0" x2="0" y2="1"><stop offset="0" stop-color="#e0369f" stop-opacity=".5"/><stop offset="1" stop-color="#e0369f" stop-opacity="0"/></linearGradient></defs>
      <path d="M0 18 Q8 6 16 16 T32 16 T48 16 T64 16 T80 14 L90 10 L90 36 L0 36Z" fill="url(#gp)"/>
      <path d="M0 18 Q8 6 16 16 T32 16 T48 16 T64 16 T80 14 L90 10" fill="none" stroke="#d10ea8" stroke-width="1"/>
    </svg>
  </div>
  <div class="abs stat-card gross">
    <h4>GROSS SALES</h4>
    <p>$2300</p>
    <svg width="108" height="44" viewBox="0 0 108 44" style="margin-top:4px">
      <defs><linearGradient id="gb" x1="0" y1="0" x2="0" y2="1"><stop offset="0" stop-color="#5b6cf0" stop-opacity=".55"/><stop offset="1" stop-color="#5b6cf0" stop-opacity="0"/></linearGradient></defs>
      <path d="M0 18 Q9 2 18 14 T36 14 T54 14 T72 14 T90 14 L108 12 L108 44 L0 44Z" fill="url(#gb)"/>
      <path d="M0 18 Q9 2 18 14 T36 14 T54 14 T72 14 T90 14 L108 12" fill="none" stroke="#4b5ce0" stroke-width="1"/>
    </svg>
  </div>
</section>

<section>
  <div class="abs dark"></div>
  <h2 class="abs dark-title">TRANSFORMING DATA<br>INTO <em>ACTIONABLE</em> INTELLIGENCE</h2>
  <p class="abs dark-text">Lorem Ipsum is simply dummy text of the printing and typesetting industry. Lorem Ipsum has been the industry's standard dummy text ever since the 1500s,</p>

  <article class="abs service" style="left:71px">
    <svg width="26" height="24" viewBox="0 0 26 24" fill="none" stroke="#d10ea8" stroke-width="2">
      <rect x="2" y="2" width="22" height="15" rx="1"/><path d="M9 22h8M13 17v5"/><path d="M7 13V9M11 13V6M15 13V8M19 13v-3" stroke-width="1.6"/>
    </svg>
    <h3>DATA ANALYTICS</h3>
    <p>Lorem Ipsum is simply dummy text of the printing and typesetting industry. Lorem Ipsum has been the industry's standard dummy text ever since the 1500s,</p>
  </article>
  <article class="abs service" style="left:345px">
    <svg width="28" height="26" viewBox="0 0 28 26" fill="#d10ea8">
      <circle cx="14" cy="14" r="8"/><circle cx="14" cy="14" r="3.5" fill="#1a1263"/>
      <g><rect x="12.5" y="2" width="3" height="5"/><rect x="12.5" y="21" width="3" height="5"/><rect x="2" y="12.5" width="5" height="3"/><rect x="21" y="12.5" width="5" height="3"/></g>
    </svg>
    <h3>PROFESSIONAL SERVICES</h3>
    <p>Lorem Ipsum is simply dummy text of the printing and typesetting industry. Lorem Ipsum has been the industry's standard dummy text ever since the 1500s,</p>
  </article>
  <div class="abs toggle" style="left:191px"><svg width="8" height="6" viewBox="0 0 8 6"><path d="M1 1l3 3 3-3" fill="none" stroke="#fff" stroke-width="1.6"/></svg></div>
  <div class="abs toggle" style="left:465px"><svg width="8" height="6" viewBox="0 0 8 6"><path d="M1 1l3 3 3-3" fill="none" stroke="#fff" stroke-width="1.6"/></svg></div>
</section>

<section>
  <h2 class="abs contact-title">YOUR DATA, OUR<br><em>EXPERTISE</em></h2>
  <p class="abs contact-text">Lorem Ipsum is simply dummy text of the printing and typesetting industry. Lorem Ipsum has been the industry's standard dummy text ever since the 1500s,</p>

  <div class="abs info" style="top:944px">
    <div class="ico"><svg width="10" height="10" viewBox="0 0 10 10"><path d="M2 1l2 2-1 1.5c.6 1.2 1.3 1.9 2.5 2.5L7 6l2 2-1.5 1.5C4 9 1 6 .5 2.5z" fill="#fff"/></svg></div>
    <div><h5>Call Now</h5><span>123-456-7890</span></div>
  </div>
  <div class="abs info" style="top:983px">
    <div class="ico"><svg width="11" height="8" viewBox="0 0 11 8"><rect x=".5" y=".5" width="10" height="7" fill="none" stroke="#fff"/><path d="M.5 .5l5 4 5-4" fill="none" stroke="#fff"/></svg></div>
    <div><h5>Email Us</h5><span>info@northgrid.example</span></div>
  </div>
  <div class="abs info" style="top:1022px">
    <div class="ico"><svg width="8" height="11" viewBox="0 0 8 11"><path d="M4 0a4 4 0 0 1 4 4c0 3-4 7-4 7S0 7 0 4a4 4 0 0 1 4-4z" fill="#fff"/><circle cx="4" cy="4" r="1.5" fill="#0f0a45"/></svg></div>
    <div><h5>Address</h5><span>Lorem ipsum is a<br>dummy text</span></div>
  </div>

  <form class="abs form">
    <h3>GET IN TOUCH WITH US</h3>
    <div class="rule"></div>
    <div class="field" style="top:56px;height:21px;line-height:21px">Name</div>
    <div class="field" style="top:82px;height:21px;line-height:21px">Email</div>
    <div class="field" style="top:108px;height:80px;padding-top:6px">Message</div>
    <div class="send"><svg width="10" height="10" viewBox="0 0 10 10"><path d="M9 1L1 4.5l3 1 1 3.5z" fill="#fff"/></svg></div>
  </form>
</section>

<footer>
  <div class="abs footer"></div>
  <div class="abs logo footer-logo">NORTHGRID</div>
  <div class="abs copyright">© 2023-Northgrid</div>
</footer>
</body>
</html>
```